Business Card Design - TORVEX
miles@torvex.example
Project: Business Card Design - TORVEX
Business Card Design - TORVEX - Telecommunications
Creative Brief
Professional
Miles Brandt
Vice President
www.torvex.example
Looking for a very well designed and eye catching business card that we can use into the future. Should be designed around the TORVEX logo and using the included radio images is just optional.
Digital Communications Coastline Fleet Relay Grid Cellphone Coverage Enhancement P25 - Public Safety Equipment Digital Radio Rentals Dispatch Consoles
milestor7 milestor7
Thanks for all the design ideas so far. I will be getting together with my team and will start providing feedback this afternoon. Best Wishes, Miles

```html
<!DOCTYPE html>
<html lang="en">
<head>
<meta charset="utf-8">
<title>TORVEX Business Card</title>
<link rel="stylesheet" href="https://fonts.googleapis.com/css2?family=Michroma&display=swap">
<style>
  :root {
    --bg: #e4e5e7;
    --charcoal: #2a2b2e;
    --charcoal-light: #3a3b3f;
    --paper: #ffffff;
    --red: #d3202a;
    --ink: #2a2b2e;
    --muted: #c9cacc;
    --radio: #7d8086;
  }
  * { box-sizing: border-box; margin: 0; padding: 0; }
  html, body {
    width: 1200px; height: 901px; overflow: hidden;
    background: var(--bg);
    font-family: "Michroma", sans-serif;
  }
  .stage { position: relative; width: 1200px; height: 901px; }

  .card {
    position: absolute;
    width: 560px; height: 320px;
    box-shadow: 0 10px 30px rgba(0,0,0,.18);
    overflow: hidden;
  }

  /* Front card */
  .card--front {
    left: 80px; top: 470px;
    background: var(--paper);
    display: flex;
    border-bottom: 5px solid var(--red);
  }
  .front__panel {
    width: 66%;
    background: linear-gradient(160deg, var(--charcoal-light), var(--charcoal));
    border-left: 5px solid var(--red);
    padding: 44px 0 0 38px;
    color: var(--paper);
  }
  .brand {
    display: flex; align-items: center; gap: 10px;
    font-size: 34px; letter-spacing: 4px;
  }
  .brand__dot { width: 12px; height: 12px; background: var(--red); }
  .front__panel .brand { color: var(--paper); }
  .person { margin-top: 42px; }
  .person__name { font-size: 15px; letter-spacing: 2px; }
  .person__title { font-size: 9px; color: var(--red); letter-spacing: 1.5px; margin-top: 6px; }
  .contacts { list-style: none; margin-top: 20px; }
  .contacts li {
    display: flex; align-items: center; gap: 10px;
    font-size: 10px; letter-spacing: 1px; margin-bottom: 9px; color: var(--muted);
  }
  .contacts svg { width: 13px; height: 13px; flex: none; }
  .front__media {
    flex: 1; display: flex; align-items: flex-end; justify-content: center;
    padding-bottom: 22px;
  }

  .radio-image {
    width: 70px; height: 190px;
    border-radius: 8px;
    background: linear-gradient(180deg, var(--radio), var(--charcoal));
  }

  /* Back card */
  .card--back {
    left: 580px; top: 90px;
    background: var(--paper);
    border-bottom: 5px solid var(--red);
    display: flex; align-items: center;
    padding: 0 40px 0 50px;
  }
  .back__media { width: 90px; display: flex; justify-content: center; }
  .back__media .radio-image { height: 170px; width: 62px; }
  .back__content { margin-left: 36px; }
  .card--back .brand { color: var(--ink); font-size: 30px; }
  .services { list-style: none; margin-top: 20px; }
  .services li {
    display: flex; align-items: center; gap: 9px;
    font-size: 9.5px; letter-spacing: .8px; color: var(--ink);
    margin-bottom: 9px; text-transform: uppercase;
  }
  .services li::before {
    content: ""; width: 5px; height: 5px; border-radius: 50%;
    background: var(--ink); flex: none;
  }
  .services .lead { color: var(--red); }
</style>
</head>
<body>
<main class="stage">

  <section class="card card--back">
    <div class="back__media">
      <div class="radio-image" role="img" aria-label="Photo of a handheld two-way digital radio"></div>
    </div>
    <div class="back__content">
      <div class="brand"><span class="brand__dot"></span>TORVEX</div>
      <ul class="services">
        <li><span><span class="lead">Digital</span> Communications</span></li>
        <li><span><span class="lead">Coastline</span> Fleet Relay Grid</span></li>
        <li><span><span class="lead">Cellphone</span> Coverage Enhancement</span></li>
        <li><span><span class="lead">P25</span> Public Safety Equipment</span></li>
        <li><span><span class="lead">Digital</span> Radio Rentals</span></li>
        <li><span><span class="lead">Dispatch</span> Consoles</span></li>
      </ul>
    </div>
  </section>

  <section class="card card--front">
    <div class="front__panel">
      <div class="brand"><span class="brand__dot"></span>TORVEX</div>
      <div class="person">
        <p class="person__name">MILES BRANDT</p>
        <p class="person__title">VICE PRESIDENT</p>
      </div>
      <ul class="contacts">
        <li>
          <svg viewBox="0 0 24 24" fill="var(--red)"><path d="M6.6 10.8a15 15 0 0 0 6.6 6.6l2.2-2.2a1 1 0 0 1 1-.25 11.4 11.4 0 0 0 3.6.57 1 1 0 0 1 1 1V20a1 1 0 0 1-1 1A17 17 0 0 1 3 4a1 1 0 0 1 1-1h3.5a1 1 0 0 1 1 1c0 1.25.2 2.45.57 3.57a1 1 0 0 1-.25 1z"/></svg>
          555-014-2290
        </li>
        <li>
          <svg viewBox="0 0 24 24" fill="none" stroke="var(--red)" stroke-width="2"><rect x="3" y="5" width="18" height="14"/><path d="M3 6l9 7 9-7"/></svg>
          miles@torvex.example
        </li>
        <li>
          <svg viewBox="0 0 24 24" fill="none" stroke="var(--red)" stroke-width="2"><circle cx="12" cy="12" r="9"/><path d="M3 12h18M12 3c3 3 3 15 0 18M12 3c-3 3-3 15 0 18"/></svg>
          www.torvex.example
        </li>
      </ul>
    </div>
    <div class="front__media">
      <div class="radio-image" role="img" aria-label="Photo of a handheld two-way digital radio"></div>
    </div>
  </section>

</main>
</body>
</html>
```